M Zyvantics Buisness Cards

I need a technology focused clean business card for my employees. I have attached out logo to include in the mocks. We're a modern tech consulting firm that drives to interface humanity with technology in a truly cohesive fashion.

```html
<!DOCTYPE html>
<html lang="en">
<head>
<meta charset="utf-8">
<title>M Zyvantics Business Cards</title>
<link rel="stylesheet" href="https://fonts.googleapis.com/css2?family=Open+Sans:wght@400;600&family=Bebas+Neue&display=swap">
<style>
  :root {
    --page-bg: #c4c5c8;
    --card-white: #ffffff;
    --brand-blue-light: #6f8fc0;
    --brand-blue: #3b64a3;
    --brand-blue-dark: #1f3d72;
    --band-blue: #2f5491;
    --mark-grey: #6b6c6f;
    --logo-grey: #7c7e82;
    --accent-blue: #3d6bc0;
    --text-light: #ffffff;
  }
  html, body {
    margin: 0;
    padding: 0;
    width: 1200px;
    height: 1200px;
    overflow: hidden;
    background: var(--page-bg);
  }
  .canvas {
    position: relative;
    width: 1200px;
    height: 1200px;
  }
  .card {
    position: absolute;
    top: 250px;
    width: 400px;
    height: 700px;
    overflow: hidden;
    box-shadow: 0 10px 30px rgba(0,0,0,0.18);
  }
  .card--front { left: 170px; }
  .card--back {
    left: 630px;
    background: linear-gradient(160deg, var(--brand-blue-light) 0%, var(--brand-blue) 45%, var(--brand-blue-dark) 100%);
  }
  .card-art {
    position: absolute;
    inset: 0;
  }
  .brand {
    position: absolute;
    top: 95px;
    left: 0;
    right: 0;
    display: flex;
    align-items: center;
    justify-content: center;
    gap: 12px;
    font-family: "Open Sans", sans-serif;
    font-weight: 600;
    font-size: 38px;
    color: var(--logo-grey);
    letter-spacing: 0.5px;
  }
  .brand-dot {
    width: 18px;
    height: 18px;
    border-radius: 50%;
    background: var(--accent-blue);
  }
  .details {
    position: absolute;
    top: 395px;
    left: 0;
    right: 0;
    text-align: center;
    font-family: "Open Sans", sans-serif;
    color: var(--text-light);
  }
  .details__name {
    margin: 0;
    font-size: 30px;
    font-weight: 400;
    letter-spacing: 0.5px;
  }
  .details__role {
    margin: 4px 0 34px;
    font-size: 17px;
  }
  .details__contact,
  .details__address {
    margin: 0;
    font-size: 18px;
    line-height: 1.45;
  }
  .details__address { margin-top: 30px; }
  .back-title {
    position: absolute;
    top: 290px;
    left: 0;
    right: 0;
    text-align: center;
    font-family: "Bebas Neue", sans-serif;
    color: var(--text-light);
    font-size: 58px;
    line-height: 0.95;
    letter-spacing: 1px;
  }
</style>
</head>
<body>
<main class="canvas">

  <section class="card card--front" aria-label="Business card front">
    <svg class="card-art" width="400" height="700" viewBox="0 0 400 700" aria-hidden="true">
      <defs>
        <linearGradient id="frontFill" x1="0" y1="0" x2="0.6" y2="1">
          <stop offset="0" stop-color="#7a98c6"/>
          <stop offset="0.5" stop-color="#3f67a6"/>
          <stop offset="1" stop-color="#1f3d72"/>
        </linearGradient>
        <linearGradient id="bandFill" x1="0" y1="0" x2="1" y2="0">
          <stop offset="0" stop-color="#3a63a8"/>
          <stop offset="0.5" stop-color="#26477f"/>
          <stop offset="1" stop-color="#4a75bb"/>
        </linearGradient>
      </defs>
      <rect width="400" height="700" fill="url(#frontFill)"/>
      <path d="M0 0 H400 V200 C330 300 70 300 0 200 Z" fill="var(--card-white)"/>
      <path d="M0 228 C70 318 330 318 400 228" fill="none" stroke="var(--card-white)" stroke-width="34"/>
      <path d="M0 228 C70 318 330 318 400 228" fill="none" stroke="url(#bandFill)" stroke-width="24"/>
      <circle cx="200" cy="300" r="50" fill="var(--card-white)"/>
      <circle cx="200" cy="300" r="39" fill="var(--mark-grey)"/>
    </svg>

    <div class="brand">
      <span class="brand-dot"></span>
      <span class="brand-name">M Zyvantics</span>
    </div>

    <div class="details">
      <h1 class="details__name">JOHN DOE</h1>
      <p class="details__role">Director</p>
      <p class="details__contact">1-234-567890<br>www.mzyvantics.com<br>john@mzyvantics.com</p>
      <p class="details__address">Dummy city<br>Dummy Country Land</p>
    </div>
  </section>

  <section class="card card--back" aria-label="Business card back">
    <div class="back-title">M<br>ZYVANTICS</div>
  </section>

</main>
</body>
</html>
```